Ledgerforge Studio - WordPress Theme & Logo

Design a logo and Wordpress website design for Ledgerforge Studio. Ledgerforge Studio provides cryptocurrency development services to clients who need a team to create & continue developing a new cryptocurrency or who want to replace their current cryptocurrency development team. more details in the attached document.
Updates

Target Market(s)

Entrepreneurs who are building a business / platform that makes use of an underlying cryptocurrency.

Logo Text

LS or Ledgerforge Studio

Coding

Coded - Design and coding required

Font styles to use
Sans Serif

Requirements
Must have
• Professional logo, complete coded Wordpress theme for all pages, containing all specified links and buttons
Nice to have
• It would be nice if the buttons that are meant to integrate with Dealcurrent contain the necessary code for that. I can provide any necessary Dealcurrent details from my account.
Should not have
• Slow loading time

```html
<!DOCTYPE html>
<html lang="en">
<head>
<meta charset="utf-8">
<title>Ledgerforge Studio</title>
<link href="https://fonts.googleapis.com/css2?family=Poppins:wght@400;500;600;700&display=swap" rel="stylesheet">
<style>
:root{
  --blue:#0b4fa0;
  --blue-band:#0b55a8;
  --cyan:#1fbcec;
  --cyan-btn:#4cc6f4;
  --ink:#1a1a1a;
  --text:#333;
  --muted:#555;
  --grey-bg:#f1f1f1;
  --dark:#1d1f22;
  --footer:#232527;
  --white:#fff;
}
*{box-sizing:border-box;margin:0;padding:0}
html,body{width:1200px;height:3054px;overflow:hidden;background:var(--white)}
body{font-family:'Poppins',sans-serif;color:var(--text);position:relative}
.abs{position:absolute}
a{color:inherit;text-decoration:none}

/* header */
.site-header{left:0;top:0;width:1200px;height:76px;background:var(--white)}
.brand{display:flex;align-items:center;gap:10px}
.brand-mark{width:44px;height:44px;border-radius:50%;border:4px solid var(--blue);display:flex;align-items:center;justify-content:center;font-weight:700;font-size:15px;color:var(--blue)}
.brand-name{font-weight:600;font-size:22px;line-height:24px;color:var(--blue)}
.site-header .brand{left:88px;top:12px}
.main-nav{left:0;top:28px;font-size:13.5px;color:var(--ink)}
.main-nav a{position:absolute;white-space:nowrap}
.header-cta{left:952px;top:15px;width:159px;height:47px;background:var(--blue);color:var(--white);font-size:12.5px;line-height:15px;text-align:center;padding-top:8px;border-radius:2px}
.header-cta b{font-weight:600}

/* hero */
.hero{left:0;top:76px;width:1200px;height:450px}
.hero-bg{left:0;top:0;width:1200px;height:450px;background:radial-gradient(ellipse at 75% 35%,#1d6c86 0%,#134a63 35%,#0c2736 75%,#0a1e2a 100%)}
.hero-title{left:0;top:137px;width:1200px;text-align:center;font-weight:700;font-size:38px;color:var(--cyan);letter-spacing:.3px}
.hero-sub{left:0;top:180px;width:1200px;text-align:center;font-size:22px;color:var(--white)}
.hero-btn{left:461px;top:228px;width:279px;height:37px;background:var(--cyan-btn);color:var(--ink);font-size:15px;line-height:37px;text-align:center;border-radius:2px}
.hero-btn b{font-weight:600}
.slide-arrow{width:28px;height:28px}

/* intro */
.intro{left:155px;top:572px;width:890px;text-align:center;font-size:15.2px;line-height:21px;color:var(--ink)}

/* why */
.why{left:0;top:709px;width:1200px;height:364px;background:var(--grey-bg)}
.section-title{text-align:center;font-weight:600;color:var(--ink);font-size:26px;width:1200px;left:0}
.why .section-title{top:72px}
.feature{width:260px;text-align:center}
.feature svg{display:block;margin:0 auto}
.feature h3{font-weight:500;font-size:17.5px;color:var(--ink);margin-top:12px}
.feature p{font-size:13.5px;line-height:18px;color:var(--muted);margin-top:4px}

/* about */
.about-photo{left:88px;top:1154px;width:452px;height:340px;background:linear-gradient(135deg,#c9d3dc 0%,#7f98ae 40%,#2c4a6a 70%,#8e9ea8 100%)}
.about-title{left:620px;top:1190px;font-weight:600;font-size:30px;color:var(--ink)}
.about-text{left:620px;width:430px;font-size:13.5px;line-height:19px;color:var(--ink)}
.btn-outline{left:620px;top:1418px;width:110px;height:32px;border:1px solid #888;border-radius:3px;font-size:11.5px;line-height:30px;text-align:center;color:var(--ink)}

/* testimonials */
.testimonials{left:0;top:1575px;width:1200px;height:433px;background:linear-gradient(180deg,#26282b 0%,#16181a 100%)}
.testimonials h2{position:absolute;left:0;top:72px;width:1200px;text-align:center;font-weight:700;font-size:31px;color:var(--cyan)}
.t-card{top:149px;width:325px;height:204px;background:var(--white);text-align:center}
.t-card .quote{display:block;margin:20px auto 0}
.t-card p{font-size:13px;line-height:17.5px;color:var(--ink);padding:0 28px;margin-top:14px}
.t-person{display:flex;align-items:center;justify-content:center;gap:10px;margin-top:18px;font-size:13px;font-weight:500;color:var(--ink)}
.avatar{width:40px;height:40px;border-radius:50%;background:linear-gradient(135deg,#b9a08c,#5d4a40)}

/* services */
.services-title{top:2080px}
.s-card{top:2148px;width:325px;height:404px;background:var(--white);box-shadow:0 0 10px rgba(0,0,0,.06)}
.s-card .s-img{width:325px;height:188px}
.s-card h3{font-weight:500;font-size:17px;color:var(--ink);margin:28px 24px 0}
.s-card .s-body{font-size:14px;line-height:20.5px;color:var(--ink);margin:16px 24px 0}
.s-card ul{list-style:none;font-size:13.5px;line-height:18.5px;color:var(--ink);margin:14px 24px 0 24px}
.s-card li{position:relative;padding-left:11px}
.s-card li::before{content:"";position:absolute;left:0;top:6px;border-left:4px solid currentColor;border-top:3px solid transparent;border-bottom:3px solid transparent}
.s-card.featured{background:#333537}
.s-card.featured h3{color:var(--cyan);font-weight:600}
.s-card.featured ul{color:var(--white)}

/* cta band */
.cta-band{left:160px;top:2633px;width:880px;height:90px;background:var(--blue-band);border-radius:4px 4px 0 0;z-index:2}
.cta-band span{position:absolute;left:185px;top:27px;font-weight:500;font-size:28px;color:var(--white)}
.cta-arrow{position:absolute;left:604px;top:28px;width:90px;height:33px;background:var(--white);border-radius:2px}

/* footer */
.site-footer{left:0;top:2723px;width:1200px;height:294px;background:linear-gradient(160deg,#2a2c2e 0%,#1c1e20 100%)}
.site-footer .brand{position:absolute;left:130px;top:82px}
.site-footer .brand-mark{border-color:var(--blue);color:var(--blue)}
.site-footer .brand-name{color:var(--cyan)}
.foot-head{position:absolute;font-weight:600;font-size:16.5px;color:var(--cyan)}
.foot-links a{position:absolute;font-size:13.5px;color:var(--white)}
.foot-links a.active{color:var(--cyan);border-bottom:1px solid var(--cyan)}
.newsletter{position:absolute;left:848px;top:109px;width:263px;height:37px;background:var(--white);border:1px solid #ccc}
.newsletter span{position:absolute;left:26px;top:9px;font-size:12px;color:#777}
.newsletter b{position:absolute;right:2px;top:2px;width:38px;height:31px;background:var(--blue);color:var(--white);font-size:12px;font-weight:600;text-align:center;line-height:31px}
.social{position:absolute;top:176px;width:14px;height:14px;border-radius:50%;background:var(--white)}
.social.on{background:var(--cyan)}
.copyright{left:0;top:3017px;width:1200px;height:37px;background:var(--blue-band);color:var(--white);text-align:center;font-size:13px;line-height:37px}
</style>
</head>
<body>

<header class="site-header abs">
  <div class="brand abs"><div class="brand-mark">LS</div><div class="brand-name">Ledgerforge<br>Studio</div></div>
  <nav class="main-nav abs">
    <a style="left:478px">About</a>
    <a style="left:544px">Testimonials</a>
    <a style="left:652px">Services</a>
    <a style="left:734px">Book a Consultation</a>
    <a style="left:889px">Blog</a>
  </nav>
  <a class="header-cta abs">Schedule a<br><b>FREE CONSULTATION</b></a>
</header>

<section class="hero abs">
  <div class="hero-bg abs" role="img" aria-label="Dark teal network of connected nodes over financial chart data"></div>
  <svg class="abs" style="left:0;top:390px" width="1200" height="60" viewBox="0 0 1200 60">
    <polygon points="0,40 600,12 1200,40 1200,60 0,60" fill="#4fc3f7"/>
    <polygon points="0,52 600,22 1200,52 1200,60 0,60" fill="#fff"/>
  </svg>
  <h1 class="hero-title abs">YOUR OWN CRYPTOCURRENCY.</h1>
  <p class="hero-sub abs">Secure, easy to use, and built by an expert team.</p>
  <a class="hero-btn abs">Schedule a <b>Free Consultation</b></a>
  <svg class="slide-arrow abs" style="left:46px;top:202px" viewBox="0 0 28 28"><circle cx="14" cy="14" r="12" fill="none" stroke="#888" stroke-width="2"/><path d="M20 14H8M12 9l-5 5 5 5" fill="none" stroke="#888" stroke-width="2"/></svg>
  <svg class="slide-arrow abs" style="left:1124px;top:202px" viewBox="0 0 28 28"><circle cx="14" cy="14" r="12" fill="none" stroke="#4fc3f7" stroke-width="2"/><path d="M8 14h12M16 9l5 5-5 5" fill="none" stroke="#4fc3f7" stroke-width="2"/></svg>
</section>

<p class="intro abs">Ledgerforge Studio adds professionalism to cryptocurrency development. Our done-for-you service covers everything from development and IT operations to ongoing support. You have access to a full team, for less than the typical cost of a single developer.</p>

<section class="why abs">
  <h2 class="section-title abs">WHY CHOOSE LEDGERFORGE STUDIO</h2>
  <div class="feature abs" style="left:153px;top:160px">
    <svg width="46" height="48" viewBox="0 0 46 48" fill="none" stroke="#0b4fa0" stroke-width="2.4"><path d="M23 2v6M8 6l4 5M38 6l-4 5"/><path d="M6 22l7-8h20l7 8-17 22z"/><path d="M6 22h34M17 14l-4 8 10 22 10-22-4-8"/></svg>
    <h3>Value</h3>
    <p>A team of experts, regular updates,<br>and fixed costs</p>
  </div>
  <div class="feature abs" style="left:469px;top:160px">
    <svg width="48" height="48" viewBox="0 0 48 48" fill="none" stroke="#0b4fa0" stroke-width="2.4"><path d="M10 26v-6a14 14 0 0128 0v6"/><rect x="6" y="24" width="8" height="14" rx="3"/><rect x="34" y="24" width="8" height="14" rx="3"/><path d="M38 38c0 5-6 7-12 7"/><rect x="22" y="42" width="6" height="5" rx="2"/></svg>
    <h3>Support</h3>
    <p>Receive advice and other<br>services, beyond development.</p>
  </div>
  <div class="feature abs" style="left:794px;top:160px">
    <svg width="56" height="48" viewBox="0 0 56 48" fill="none" stroke="#0b4fa0" stroke-width="2.4" stroke-linejoin="round"><path d="M2 14l10-8 8 4 8-4 8 4 8-4 10 8-8 14-10 10-8-4-8 4-10-10z"/><path d="M20 10l-6 10 8 2 6-6 10 10M18 30l4 4M24 28l6 6M30 24l6 6"/></svg>
    <h3>Commitment</h3>
    <p>Enjoy regular updates and<br>new features.</p>
  </div>
</section>

<div class="about-photo abs" role="img" aria-label="Office team reviewing analytics charts on a large wall screen"></div>
<h2 class="about-title abs">ABOUT US</h2>
<p class="about-text abs" style="top:1250px">In addition to creating and enhancing cryptocurrencies for clients, the Ledgerforge Studio team has been running the Veltrix crypto­currency since 2017.</p>
<p class="about-text abs" style="top:1326px">We prefer long-term relationships, enabling us to deliver the very highest quality and giving you peace of mind that you've got a professional and trustworthy team at your side.</p>
<a class="btn-outline abs">READ MORE</a>

<section class="testimonials abs" role="region" aria-label="Testimonials over a dimmed photo of a seated audience">
  <h2>TESTIMONIALS</h2>
  <div class="t-card abs" style="left:89px">
    <svg class="quote" width="24" height="20" viewBox="0 0 24 20" fill="#cfcfcf"><path d="M0 0h10v10l-4 10H2l3-10H0zM14 0h10v10l-4 10h-4l3-10h-5z"/></svg>
    <p>Lorem Ipsum is simply dummy text of the printing and typesetting industry. Lorem Ipsum has been the industry's standard dummy text ever since the 1500s</p>
    <div class="t-person"><div class="avatar" role="img" aria-label="Client portrait"></div>Jordan M.</div>
  </div>
  <div class="t-card abs" style="left:439px">
    <svg class="quote" width="24" height="20" viewBox="0 0 24 20" fill="#cfcfcf"><path d="M0 0h10v10l-4 10H2l3-10H0zM14 0h10v10l-4 10h-4l3-10h-5z"/></svg>
    <p>Lorem Ipsum is simply dummy text of the printing and typesetting industry. Lorem Ipsum has been the industry's standard dummy text ever since the 1500s</p>
    <div class="t-person"><div class="avatar" role="img" aria-label="Client portrait"></div>Jordan M.</div>
  </div>
  <div class="t-card abs" style="left:789px">
    <svg class="quote" width="24" height="20" viewBox="0 0 24 20" fill="#1a1a1a"><path d="M0 0h10v10l-4 10H2l3-10H0zM14 0h10v10l-4 10h-4l3-10h-5z"/></svg>
    <p>Lorem Ipsum is simply dummy text of the printing and typesetting industry. Lorem Ipsum has been the industry's standard dummy text ever since the 1500s</p>
    <div class="t-person"><div class="avatar" role="img" aria-label="Client portrait" style="background:linear-gradient(135deg,#d4b49a,#7a5a46)"></div>Jordan M.</div>
  </div>
  <svg class="abs" style="left:1137px;top:241px" width="18" height="18" viewBox="0 0 18 18"><circle cx="9" cy="9" r="7.5" fill="none" stroke="#1fbcec" stroke-width="1.8"/><path d="M5 9h8M10 6l3 3-3 3" fill="none" stroke="#1fbcec" stroke-width="1.8"/></svg>
</section>

<h2 class="section-title services-title abs">SERVICES</h2>
<article class="s-card abs" style="left:89px">
  <div class="s-img" role="img" aria-label="Trader at a laptop showing market charts" style="background:linear-gradient(120deg,#3a2a24 0%,#8a5a46 45%,#d8c4b8 100%)"></div>
  <h3>Blockchain Creation &amp; Launch</h3>
  <p class="s-body">Base fixed price for cryptocurrency de­velopment &amp; launch</p>
  <p class="s-body" style="margin-top:18px">--would be customizable based on client requirements</p>
</article>
<article class="s-card abs" style="left:438px">
  <div class="s-img" role="img" aria-label="Lower costs concept with business icons in hexagons" style="background:radial-gradient(circle at 50% 50%,#c86a2a 0%,#5a2e16 45%,#1d1410 100%)"></div>
  <h3>Basic offering</h3>
  <ul>
    <li>Lower cost per month</li>
    <li>Slower release schedule (about every 3 months)</li>
    <li>Client assists with testing new releases</li>
    <li>Less input into future roadmap/features</li>
    <li>Limited support hours/priority (always available for emergencies)</li>
  </ul>
</article>
<article class="s-card featured abs" style="left:786px">
  <div class="s-img" role="img" aria-label="Hand reviewing a financial report on a clipboard in blue tones" style="background:linear-gradient(135deg,#2f5d9a 0%,#7ea4d2 55%,#c9daf0 100%)"></div>
  <h3>Full service offering</h3>
  <ul>
    <li>Mid-range cost per month</li>
    <li>Releases every 1.5 - 2 months</li>
    <li>Client can help request/prioritize new fea­tures</li>
    <li>Full testing by my team prior to release</li>
    <li>Priority support during normal business hours, always available for emergencies</li>
  </ul>
</article>

<div class="cta-band abs">
  <span>Schedule a Free Consultation</span>
  <div class="cta-arrow"><svg width="90" height="33" viewBox="0 0 90 33"><path d="M32 16.5h24M49 10l7 6.5-7 6.5" fill="none" stroke="#0b4fa0" stroke-width="3"/></svg></div>
</div>

<footer class="site-footer abs">
  <div class="brand"><div class="brand-mark">LS</div><div class="brand-name">Ledgerforge<br>Studio</div></div>
  <div class="foot-head" style="left:515px;top:67px">Quick Links</div>
  <nav class="foot-links">
    <a style="left:515px;top:104px">Home</a>
    <a class="active" style="left:515px;top:132px">About</a>
    <a style="left:515px;top:160px">Feature</a>
    <a style="left:515px;top:188px">Pricing</a>
    <a style="left:515px;top:216px">Contact</a>
    <a style="left:662px;top:104px">Blog</a>
    <a style="left:662px;top:132px">Search</a>
    <a style="left:662px;top:160px">T &amp; Cs</a>
    <a style="left:662px;top:188px">Privacy</a>
  </nav>
  <div class="foot-head" style="left:847px;top:68px">Get Our Newsletter</div>
  <div class="newsletter"><span>Enter email address</span><b>GO</b></div>
  <span class="social" style="left:846px"></span>
  <span class="social" style="left:882px"></span>
  <span class="social on" style="left:921px"></span>
  <span class="social" style="left:962px"></span>
</footer>
<div class="copyright abs">Copyright © 2021 Ledgerforge Studio. All Rights Reserved</div>

</body>
</html>
```